Thornwell Consulting Cover 3 - Capital Allocation battlefield

Thornwell Consulting is a business consulting firm. We will publish a series of four thought leadership pieces online and via PDF. The third of the series is attached to this project. We need an eye-catching cover page with a back page that keeps with our branding. The document attached is in the final draft, and the cover and pack pages are placeholders only. You can find more about our branding and style on our website www.thornwellconsulting.com.au. The other three projects can be found here with a similar brief, and you are welcome to submit a design for all 4.

```html
<!DOCTYPE html>
<html lang="en">
<head>
<meta charset="utf-8">
<title>Thornwell Consulting – The Capital Allocation Battlefield</title>
<link href="https://fonts.googleapis.com/css2?family=Poppins:wght@300;400;500;600;700&display=swap" rel="stylesheet">
<style>
  :root {
    --board: #5a5859;
    --blue: #0b7fc1;
    --sky: #00a9eb;
    --orange: #e07b14;
    --orange-soft: #f08a1c;
    --white: #ffffff;
    --paper: #f4f5f7;
    --navy: #1d3b6e;
    --photo-dark: #5d6672;
    --photo-light: #b9c2cc;
  }
  * { box-sizing: border-box; margin: 0; padding: 0; }
  html, body { width: 1200px; height: 987px; overflow: hidden; }
  body {
    background: var(--board);
    font-family: "Poppins", sans-serif;
    position: relative;
    color: var(--white);
  }
  .side-label {
    position: absolute;
    top: 68px;
    width: 300px;
    text-align: center;
    font-weight: 300;
    font-size: 43px;
    letter-spacing: 2px;
    color: var(--white);
  }
  .side-label--back { left: 178px; }
  .side-label--front { left: 716px; top: 74px; }

  .page {
    position: absolute;
    top: 153px;
    height: 778px;
    overflow: hidden;
    background: var(--paper);
  }
  .page--back { left: 85px; width: 498px; }
  .page--front { left: 607px; width: 509px; }
  .page__art { position: absolute; inset: 0; width: 100%; height: 100%; }

  .brand {
    position: absolute;
    display: flex;
    align-items: center;
    gap: 10px;
  }
  .brand__dot {
    border-radius: 50%;
    background: var(--orange-soft);
    flex: none;
  }
  .brand__name {
    font-weight: 600;
    color: var(--sky);
    line-height: 1;
  }
  .page--back .brand { left: 258px; top: 84px; }
  .page--back .brand__dot { width: 44px; height: 44px; }
  .page--back .brand__name { font-size: 20px; line-height: 21px; }
  .page--front .brand { left: 54px; top: 88px; }
  .page--front .brand__dot { width: 54px; height: 54px; }
  .page--front .brand__name { font-size: 25px; line-height: 25px; }

  .contact-cta { position: absolute; left: 66px; top: 164px; width: 220px; }
  .contact-cta__tag {
    display: inline-block;
    background: var(--orange);
    border-radius: 4px;
    padding: 1px 7px;
    font-weight: 700;
    font-size: 16px;
  }
  .contact-cta__text { margin-top: 6px; font-size: 15.5px; line-height: 19px; }

  .people { position: absolute; left: 270px; top: 548px; width: 180px; text-align: center; }
  .person + .person { margin-top: 13px; }
  .person__name { font-weight: 500; font-size: 15px; line-height: 17px; }
  .person__role { font-weight: 500; font-size: 8.5px; letter-spacing: 1.6px; color: var(--navy); }
  .person__line { font-size: 10px; line-height: 14px; display: flex; justify-content: center; align-items: center; gap: 3px; }
  .person__line--email { font-size: 7.5px; }
  .person__line svg { width: 8px; height: 8px; fill: var(--navy); }

  .cover-title {
    position: absolute; left: 52px; top: 302px;
    font-weight: 700; font-size: 37px; line-height: 40px;
  }
  .cover-title__accent { color: var(--orange-soft); }
  .cover-subtitle {
    position: absolute; left: 67px; top: 581px;
    font-weight: 700; font-size: 24px; line-height: 32px;
  }
  .cover-url {
    position: absolute; left: 219px; top: 707px;
    font-weight: 400; font-size: 17.5px;
  }
</style>
</head>
<body>
  <div class="side-label side-label--back">BACK</div>
  <div class="side-label side-label--front">FRONT</div>

  <section class="page page--back">
    <svg class="page__art" viewBox="0 0 623 973" preserveAspectRatio="none">
      <defs>
        <linearGradient id="backPhoto" x1="0" y1="0" x2="1" y2="1">
          <stop offset="0" stop-color="var(--photo-dark)"/>
          <stop offset="0.6" stop-color="var(--photo-light)"/>
          <stop offset="1" stop-color="#e8ecef"/>
        </linearGradient>
      </defs>
      <polygon points="0,15 623,395 623,735 430,625 0,355" fill="var(--blue)"/>
      <polygon points="0,355 430,625 623,735 623,820 375,973 0,973" fill="url(#backPhoto)" role="img" aria-label="Photo of glass office towers seen from below"/>
      <polygon points="430,628 623,735 623,820 375,973 0,973 0,905 240,770" fill="var(--orange)"/>
      <polygon points="375,973 623,820 623,973" fill="var(--white)"/>
    </svg>

    <div class="brand">
      <span class="brand__dot"></span>
      <span class="brand__name">Thornwell<br>Consulting</span>
    </div>

    <div class="contact-cta">
      <span class="contact-cta__tag">Contact us</span>
      <p class="contact-cta__text">to find out how Thornwell Consulting can help build your company into a market leader today.</p>
    </div>

    <div class="people">
      <div class="person">
        <p class="person__name">Marcus Thornwell</p>
        <p class="person__role">MANAGING DIRECTOR</p>
        <p class="person__line"><svg viewBox="0 0 10 10"><path d="M2 0l2 2-1 1.5c.6 1.3 1.5 2.2 2.8 2.8L7.3 5 10 7 8.6 9.6C4 9.4.6 6 .4 1.4z"/></svg>+61 400 118 362</p>
        <p class="person__line person__line--email"><svg viewBox="0 0 10 10"><rect x="0" y="2" width="10" height="7" rx="1"/></svg>marcus@thornwellconsulting.com.au</p>
      </div>
      <div class="person">
        <p class="person__name">Henry Thornwell</p>
        <p class="person__role">MANAGING DIRECTOR</p>
        <p class="person__line"><svg viewBox="0 0 10 10"><path d="M2 0l2 2-1 1.5c.6 1.3 1.5 2.2 2.8 2.8L7.3 5 10 7 8.6 9.6C4 9.4.6 6 .4 1.4z"/></svg>+61 400 274 915</p>
        <p class="person__line person__line--email"><svg viewBox="0 0 10 10"><rect x="0" y="2" width="10" height="7" rx="1"/></svg>henry@thornwellconsulting.com.au</p>
      </div>
    </div>
  </section>

  <section class="page page--front">
    <svg class="page__art" viewBox="0 0 636 973" preserveAspectRatio="none">
      <defs>
        <linearGradient id="frontPhoto" x1="0" y1="0" x2="1" y2="0">
          <stop offset="0" stop-color="#8a8fa0"/>
          <stop offset="0.5" stop-color="#a7a9b8"/>
          <stop offset="1" stop-color="#d4d6de"/>
        </linearGradient>
      </defs>
      <polygon points="0,400 636,15 636,973 0,973" fill="var(--blue)"/>
      <polygon points="185,632 636,900 636,973 0,973 0,740" fill="var(--white)"/>
      <polygon points="0,740 185,632 636,905 636,973 255,973 0,820" fill="var(--orange)"/>
      <polygon points="320,690 455,70 520,30 600,25 636,45 636,890" fill="url(#frontPhoto)" role="img" aria-label="Photo of a tall stone skyscraper seen from below"/>
    </svg>

    <div class="brand">
      <span class="brand__dot"></span>
      <span class="brand__name">Thornwell<br>Consulting</span>
    </div>

    <h1 class="cover-title">The Capital<br>Allocation<br><span class="cover-title__accent">Battlefield</span></h1>
    <p class="cover-subtitle">Deploying the<br>War Chest</p>
    <p class="cover-url">thornwellconsulting.com.au</p>
  </section>
</body>
</html>
```